Velvet Compass Brochure

I would like to design an e-brochure to be sent to a particular fashion designer that we choose to invite to be featured on our platform. The brochure should reflect the existing brand image of the website. The brochure will probably have no more than four to five pages and will include the following information

1) Cover Page

2) About Us

3) Our Unique Edge

4) Member Benefits

5) Prices

6) Contact

hello designers think some people are confused about what the brochure is about i have uploaded a file with the sample text - hope this helps

Reason: Hi everyone I have extended the deadline as i have uploaded a text document for the brochure that should assist with thinking about the design. please email if you have questions

Hi I have got feedback that the document wasn't uploaded properly - the sample text to work with is now uploaded on docx format Thanks

Target Market(s)

Fashion designers

Industry/Entity Type

Fashion

Requirements
Must have
• Must be cool, edgy , contemporary and inviting

please see website www.velvetcompass.com - as look and feel should tie in with that

photos and art work can be used from website and all our social media pages

```html
<!DOCTYPE html>
<html lang="en">
<head>
<meta charset="utf-8">
<title>Velvet Compass – About Us &amp; Our Unique Edge</title>
<link href="https://fonts.googleapis.com/css2?family=Roboto:wght@300;400;500&display=swap" rel="stylesheet">
<style>
  :root {
    --backdrop: #8e8e8e;
    --paper: #ffffff;
    --ink: #2b2b2b;
    --ink-soft: #3a3a3a;
    --header-black: #1c1a1b;
    --panel-grey: #dedede;
    --portrait-light: #eef2f8;
    --portrait-mid: #c9d3e3;
    --street-dark: #2c2c2e;
    --street-mid: #6b6b6e;
    --clutch-yellow: #e8c98a;
    --clutch-teal: #3fa6c4;
  }
  * { margin: 0; padding: 0; box-sizing: border-box; }
  html, body { width: 1200px; height: 800px; overflow: hidden; }
  body {
    background: var(--backdrop);
    font-family: "Roboto", Arial, sans-serif;
    color: var(--ink);
    position: relative;
  }
  .spread {
    position: absolute;
    left: 40px; top: 30px;
    width: 1120px; height: 740px;
    display: flex;
    background: var(--paper);
  }
  .page { position: relative; width: 560px; height: 740px; overflow: hidden; }

  /* Left page: About Us */
  .portrait-photo {
    position: absolute; inset: 0;
    background: linear-gradient(160deg, var(--portrait-mid) 0%, var(--portrait-light) 45%, #ffffff 75%, var(--portrait-light) 100%);
  }
  .about {
    position: absolute;
    left: 60px; right: 50px; top: 440px;
    font-size: 12.5px; line-height: 1.45; font-weight: 400; color: var(--ink-soft);
  }
  .about h2 {
    font-weight: 500; font-size: 15px; letter-spacing: 4px;
    margin-bottom: 18px; color: var(--ink);
  }
  .about p { margin-bottom: 16px; }

  /* Right page */
  .page--edge { background: var(--paper); }
  .street-photo {
    position: absolute; left: 0; top: 0; width: 270px; height: 425px;
    background: linear-gradient(180deg, var(--street-dark) 0%, #4a4a4c 60%, var(--street-mid) 100%);
  }
  .clutch-photo {
    position: absolute; left: 0; top: 437px; width: 270px; height: 303px;
    background: linear-gradient(135deg, var(--clutch-yellow) 0%, #f1ddb0 45%, var(--clutch-teal) 100%);
  }
  .edge-header {
    position: absolute; left: 284px; top: 0; width: 276px; height: 170px;
    background: var(--header-black); color: #fff;
    padding: 34px 28px;
  }
  .edge-header h1 {
    font-weight: 400; font-size: 26px; line-height: 1.4; letter-spacing: 6px;
  }
  .edge-panel {
    position: absolute; left: 284px; top: 176px; width: 266px; height: 560px;
    background: var(--panel-grey);
    padding: 24px 16px 12px 18px;
    font-size: 10px; line-height: 1.28; color: var(--ink);
  }
  .edge-panel h3 {
    font-weight: 500; font-size: 10px; letter-spacing: 2.5px; margin-top: 10px;
  }
  .edge-panel h3:first-child { margin-top: 0; }
  .edge-panel p + p { margin-top: 8px; }
</style>
</head>
<body>
  <main class="spread">
    <section class="page page--about">
      <div class="portrait-photo" role="img" aria-label="Soft-lit portrait of a model in a white shirt wearing a long silver pendant necklace"></div>
      <div class="about">
        <h2>ABOUT US</h2>
        <p>We are so excited to invite you to join our exclusive platform!</p>
        <p>Velvet Compass takes pride in featuring edgy and independent, global designer fashion. It is a curated site where we only feature the most unique and creative designers and provide them with multiple selling opportunities to gain exposure for their brand and the designers unique vision.</p>
        <p>We know you are passionate about your design and we want to help you achieve your brand and sales goals. We know you are short on time and want a one stop solution with someone that understands your brand and cares about your image.</p>
        <p>Sound good? Read more...</p>
      </div>
    </section>

    <section class="page page--edge">
      <div class="street-photo" role="img" aria-label="Model in a white blouse and tartan skirt standing before a street mural"></div>
      <div class="clutch-photo" role="img" aria-label="Hand holding an illustrated turquoise clutch bag against a camel coat"></div>
      <header class="edge-header">
        <h1>OUR<br>UNIQUE<br>EDGE</h1>
      </header>
      <div class="edge-panel">
        <h3>EXCLUSIVE</h3>
        <p>Velvet Compass is an invite only platform. Contrary to many other sites and marketplace sites such as craftly and modaro marketplace we are VERY selective as to who we feature and will say no if the brand and designer doesn't impress. This exclusivity means that we retain our superior edge and the customer will know we are serious about representing only the best. Obviously the benefits to you the designer are obvious, we protect your brand and image.</p>
        <h3>NICHE</h3>
        <p>We don't intend to have thousands of designers on our site we know this is selfdefeating and if people have to scroll through dozens of items they will not buy as such we only sell what we love and intend to be small enough to give every designer the attention they deserve and require.</p>
        <h3>LIVE INTERACTION</h3>
        <p>As well as providing multiple outreach opportunity for your brand using our network of blogger contacts, industry contacts and pr industry contacts, we also hold exclusive fashion events at venues such a Larkspur Hall ( a members only club). Having access to such venues means that you will get exposed to the customers who can learn more of your brand and more importantly have the money to spend experimenting!</p>
        <p>We have a great blog too so will make sure we feature your prodcts when appripriate its like working with a fashion blog pr agency and shop all for one price.</p>
        <p>Seasonless fashion means that you dont have to worry about the churn you make we sell.</p>
      </div>
    </section>
  </main>
</body>
</html>
```